Consulting company business cards

We have a base design, but would be willing to update. We have a new logo/"tag" that needs to be added. Current business card design is attached for reference into our "style."

Industry/Entity Type

Business

Contact Information for Business Card

Should contain name and title, office number, mobile number if appropriate, e-mail, website, physical address, and company logo.

Font styles to use
Other font styles liked:
• See current card design on DrovankBCard

Colors
0455a3
85acd3
aaaaaa

Requirements
Must have
• Our colors are navy blue, gray, and a lighter blue
Nice to have
• Design that I can easily drop in new names/titles as we hire employees.

```html
<!DOCTYPE html>
<html lang="en">
<head>
<meta charset="utf-8">
<title>Korvell Business Card</title>
<link href="https://fonts.googleapis.com/css2?family=Roboto+Condensed:wght@400;700&display=swap" rel="stylesheet">
<style>
  :root {
    --navy: #022b4a;
    --sky: #5ba3c9;
    --paper: #eef1f6;
    --grey: #8c929a;
    --ink: #3a3f46;
    --backdrop: #dcdcec;
  }
  * { margin: 0; padding: 0; box-sizing: border-box; }
  html, body { width: 1200px; height: 906px; overflow: hidden; }
  body {
    background: var(--backdrop);
    font-family: "Roboto Condensed", Arial, sans-serif;
    position: relative;
  }
  .card {
    position: absolute;
    left: 260px;
    width: 680px;
    height: 388px;
    border-radius: 4px;
    overflow: hidden;
    box-shadow: 0 6px 18px rgba(40, 40, 80, 0.18);
  }
  .card--back { top: 50px; background: var(--navy); }
  .card--front { top: 468px; background: var(--paper); }

  .brand { position: absolute; }
  .brand__row { display: flex; align-items: center; gap: 8px; }
  .brand__name {
    font-weight: 700;
    font-size: 50px;
    letter-spacing: 3px;
    line-height: 1;
  }
  .brand__dot {
    width: 34px; height: 34px;
    border-radius: 50%;
    background: var(--sky);
  }
  .brand__tag {
    font-size: 12px;
    letter-spacing: 1.6px;
    text-transform: uppercase;
    color: var(--grey);
    margin-top: 4px;
    padding-left: 10px;
  }
  .card--back .brand { left: 82px; bottom: 110px; }
  .card--back .brand__name { color: #ffffff; }
  .card--front .brand { right: 42px; top: 48px; }
  .card--front .brand__name { color: var(--navy); }

  .person {
    position: absolute;
    left: 66px;
    top: 150px;
    padding-left: 20px;
    border-left: 5px solid var(--sky);
  }
  .person__name {
    font-weight: 700;
    font-size: 26px;
    color: var(--navy);
    text-transform: uppercase;
    letter-spacing: 0.5px;
  }
  .person__title { font-size: 18px; color: var(--navy); margin-top: 2px; }

  .contact {
    position: absolute;
    left: 70px;
    top: 240px;
    font-size: 17px;
    line-height: 21px;
    color: var(--ink);
    list-style: none;
  }
  .contact__label { color: var(--sky); font-weight: 700; }
  .address {
    position: absolute;
    left: 86px;
    top: 330px;
    font-size: 17px;
    line-height: 21px;
    color: var(--ink);
    font-style: normal;
  }
  .bands { position: absolute; left: 0; bottom: 0; }
</style>
</head>
<body>
  <section class="card card--back" aria-label="Card back">
    <div class="brand">
      <div class="brand__row">
        <span class="brand__name">KORVELL</span>
        <span class="brand__dot"></span>
      </div>
      <div class="brand__tag">A Cloud Consulting Company</div>
    </div>
  </section>

  <section class="card card--front" aria-label="Card front">
    <div class="brand">
      <div class="brand__row">
        <span class="brand__name">KORVELL</span>
        <span class="brand__dot"></span>
      </div>
      <div class="brand__tag">A Cloud Consulting Company</div>
    </div>

    <div class="person">
      <div class="person__name">Nadia Drovank</div>
      <div class="person__title">Office Manager</div>
    </div>

    <ul class="contact">
      <li><span class="contact__label">Tel:</span> 555.204.3810</li>
      <li><span class="contact__label">Fax:</span> 555.204.3871</li>
      <li><span class="contact__label">Email:</span> ndrovank@korvelltech.com</li>
      <li><span class="contact__label">Web:</span> www.korvelltech.com</li>
    </ul>

    <address class="address">1870 E Larkin Ave, Westbury<br>Ohio 45099</address>

    <svg class="bands" width="680" height="40" viewBox="0 0 680 40" aria-hidden="true">
      <polygon points="0,28 420,28 412,40 0,40" fill="var(--navy)"/>
      <polygon points="436,18 680,8 680,40 426,40" fill="var(--sky)"/>
      <polygon points="420,28 428,28 420,40 412,40" fill="var(--navy)"/>
    </svg>
  </section>
</body>
</html>
```